Volt'r Electrical Business Card Design

FRONT OF CARD: should highlight the company logo ( please use image attached) and in small font in the bottom corner must have REC 48197

BACK OF CARD : Company logo at the top, underneath the logo have my name Owen Marsh under my name in smaller font Qualified Electrician.
Details to also include are Mobile: 0438715209 E-mail: voltrelectrical@mailbox-example.net

Front and back of card please try to use similar colours as used in the logo. (Blues, greys, black and white)

The logo was created on this website so if you need a different file type of the logo please notify me.

Thanks, Owen

Industry/Entity Type

Business

Contact Information for Business Card

Details are in project description.

Colors
3176b5

Requirements
Must have
• Company logo and contact details

```html
<!DOCTYPE html>
<html lang="en">
<head>
<meta charset="utf-8">
<title>Volt'r Electrical Business Cards</title>
<link href="https://fonts.googleapis.com/css2?family=Open+Sans:wght@400;600;700&display=swap" rel="stylesheet">
<style>
  :root {
    --navy: #0f3d6e;
    --blue: #3176b5;
    --sky: #a7dcec;
    --white: #ffffff;
    --paper: #f7f8f9;
    --ink: #1d3557;
    --backdrop: #e9ecef;
  }
  * { margin: 0; padding: 0; box-sizing: border-box; }
  html, body { width: 1200px; height: 885px; overflow: hidden; }
  body {
    background: var(--backdrop);
    font-family: "Open Sans", Arial, sans-serif;
    position: relative;
  }
  .card {
    position: absolute;
    width: 520px;
    height: 315px;
    top: 285px;
    border-radius: 4px;
    overflow: hidden;
    box-shadow: 0 10px 30px rgba(0,0,0,0.18);
  }
  .card-back { left: 50px; background: var(--paper); }
  .card-front { left: 630px; background: var(--navy); }
  .card svg.art { position: absolute; inset: 0; width: 100%; height: 100%; }

  .wordmark {
    position: absolute;
    font-weight: 700;
    color: var(--navy);
    letter-spacing: 0.5px;
    white-space: nowrap;
  }
  .card-back .wordmark { top: 42px; left: 215px; font-size: 30px; }

  .holder { position: absolute; left: 32px; top: 138px; }
  .holder-name { font-size: 24px; font-weight: 700; color: var(--ink); }
  .holder-title { font-size: 15px; color: var(--sky); margin-top: -2px; }

  .contacts { position: absolute; left: 32px; top: 218px; list-style: none; }
  .contacts li {
    display: flex; align-items: center; gap: 8px;
    font-size: 13px; color: var(--ink); margin-bottom: 7px;
    white-space: nowrap;
  }
  .contacts svg { width: 16px; height: 16px; flex: none; }

  .card-front .wordmark {
    top: 130px; left: 120px; font-size: 34px;
  }
  .licence {
    position: absolute; left: 90px; top: 238px;
    font-size: 12px; font-weight: 600; color: var(--ink); letter-spacing: 0.5px;
    white-space: nowrap;
  }
</style>
</head>
<body>

<section class="card card-back" aria-label="Business card, contact side">
  <svg class="art" viewBox="0 0 520 315" aria-hidden="true">
    <polygon points="520,60 340,180 395,180 300,315 520,315" fill="var(--sky)"/>
    <polygon points="520,95 390,190 440,190 370,315 520,315" fill="var(--navy)"/>
  </svg>
  <div class="wordmark">Volt'r Electrical</div>
  <div class="holder">
    <div class="holder-name">Owen Marsh</div>
    <div class="holder-title">Qualified Electrician</div>
  </div>
  <ul class="contacts">
    <li>
      <svg viewBox="0 0 16 16" aria-hidden="true"><rect width="16" height="16" rx="2" fill="var(--blue)"/><path d="M5 4l2 2-1 1.2c.6 1.3 1.5 2.2 2.8 2.8L10 9l2 2-1.3 1.3C7.5 12 4 8.5 3.7 5.3z" fill="var(--white)"/></svg>
      0438715209
    </li>
    <li>
      <svg viewBox="0 0 16 16" aria-hidden="true"><rect width="16" height="16" rx="2" fill="var(--blue)"/><rect x="3.5" y="5" width="9" height="6.5" fill="none" stroke="var(--white)" stroke-width="1.2"/><path d="M3.5 5l4.5 3.6L12.5 5" fill="none" stroke="var(--white)" stroke-width="1.2"/></svg>
      voltrelectrical@mailbox-example.net
    </li>
  </ul>
</section>

<section class="card card-front" aria-label="Business card, logo side">
  <svg class="art" viewBox="0 0 520 315" aria-hidden="true">
    <path d="M60,38 H430 A70,70 0 0 1 500,108 V207 A70,70 0 0 1 430,277 H60 Z" fill="var(--sky)"/>
    <path d="M66,46 H428 A64,64 0 0 1 492,110 V205 A64,64 0 0 1 428,269 H66 Z" fill="var(--white)"/>
    <rect x="0" y="0" width="60" height="315" fill="var(--white)"/>
    <path d="M60,0 V315" stroke="var(--sky)" stroke-width="6"/>
    <path d="M48,0 V315" stroke="var(--navy)" stroke-width="3"/>
    <rect x="0" y="304" width="520" height="11" fill="var(--sky)"/>
  </svg>
  <div class="wordmark">Volt'r Electrical</div>
  <div class="licence">REC 48197</div>
</section>

</body>
</html>
```